Roll-Up Banner für Glückswebsite
Das war eine großartige Zusammenarbeit und unserem sehr knappen Zeitplan extrem entgegenkommend. Das design ist gleichzeitig seriös und trotzdem jung und dynamisch! Perfekt!
Zielgruppe
Die Website, www.freudenpfad.de ermöglicht es jedem Interessierten kostenlos mehr über das eigene Lebensglück, persönliche Stärken, und die eigene Lebenszufriedenheit herauszufinden. Interessierte können online Fragebögen ausfüllen, und erhalten neben einer detaillierten Rückmeldung über die eigenen Möglichkeiten und Stärken, Hinweise dazu, wie Sie an Ihrem eigenen Potenzial arbeiten können. Es handelt sich um ein Kooperationsprojekt der Nordischen Vereinigung für Heitere Seelenkunde der Uni Wendelstein, der HK-Lindau, der Health Academy Marbach und der Uni Falkenried. Zielgruppe für das Banner sind Menschen, die selbst mit Klienten im Kontext der Positiven Psychologie arbeiten oder Menschen, die sich Ihrem eigenen Lebensglück zuwenden wollen.
Aufgabenstellung
Es handelt sich um ein Roll-up Banner in den Maßen 1m Breite und 2 Meter Höhe.
Das Banner sollte so angelegt sein, dass es interessierten Besuchern auf Kongressen vermittelt, was es mit der Seite Freudenpfad.de auf sich hat. Also wissenschaftlich evaluierte kostenfreie online-Fragebögen, die Menschen dabei helfen Ihre eigenen Stärken und Potenziale zu entdecken und dem eigenen Glück näher zu kommen.
Es sollte außerdem das Logo der NVHS darauf zu sehen sein, sowie kleiner die Logos der Forschungskooperationspartner, HK-Lindau, Uni Wendelstein, Uni Falkenried, Health Academy Marbach.
Die Farben sollten zum Logo der NVHS passen.

```html
<!DOCTYPE html>
<html lang="de">
<head>
<meta charset="utf-8">
<title>Roll-Up Freudenpfad</title>
<link href="https://fonts.googleapis.com/css2?family=Fira+Sans:wght@400;600&family=PT+Sans:wght@400;700&display=swap" rel="stylesheet">
<style>
  :root {
    --navy: #1d3566;
    --navy-deep: #12295c;
    --green-light: #9dc23c;
    --green-dark: #84ae1c;
    --sky: #dfe4ea;
    --paper: #f6f7f9;
    --footer: #e6e7ea;
    --dot-1: #6cbcd6;
    --dot-2: #2a9a94;
    --dot-3: #2a9463;
    --stage: #e4e6ea;
    --white: #ffffff;
  }
  * { margin: 0; padding: 0; box-sizing: border-box; }
  html, body { width: 768px; height: 1200px; overflow: hidden; background: var(--stage); }
  body { position: relative; font-family: "PT Sans", sans-serif; color: var(--navy); }

  .banner {
    position: absolute; left: 88px; top: 20px; width: 592px; height: 1160px;
    background: var(--paper); overflow: hidden;
    box-shadow: 0 2px 10px rgba(0,0,0,.12);
  }

  .header { position: absolute; left: 0; top: 0; width: 100%; height: 124px; background: var(--paper); }
  .brand { position: absolute; left: 50px; top: 48px; display: flex; align-items: flex-start; gap: 8px; }
  .brand-dot { width: 14px; height: 14px; border-radius: 50%; background: var(--dot-2); margin-top: 3px; }
  .brand-name { font-family: "PT Sans", sans-serif; font-weight: 700; font-size: 17px; letter-spacing: 1.5px; color: var(--navy); line-height: 1; }
  .brand-sub { font-size: 6px; line-height: 7px; color: var(--navy); margin-top: 4px; }
  .site-url { position: absolute; right: 52px; top: 82px; font-size: 19px; color: var(--navy); }

  .hero { position: absolute; left: 0; top: 124px; width: 100%; height: 276px; background: linear-gradient(90deg, #e3e7ec, var(--sky)); }
  .hero-photo { position: absolute; left: 0; top: 0; width: 310px; height: 276px;
    background: radial-gradient(ellipse at 45% 45%, #c9a58c 0%, #8a6a52 35%, #cfdbe6 70%, #dfe4ea 100%); }
  .headline { position: absolute; left: 305px; width: 240px; top: 72px; text-align: center;
    font-size: 58px; line-height: 68px; font-weight: 400; color: var(--navy); }

  .content { position: absolute; left: 0; top: 400px; width: 100%; height: 613px;
    background: linear-gradient(160deg, var(--green-light) 0%, var(--green-dark) 100%); }
  .questions { position: absolute; left: 53px; top: 38px; font-family: "Fira Sans", sans-serif; font-weight: 600;
    font-size: 22px; line-height: 30px; color: var(--navy); }
  .answer-lead { position: absolute; left: 53px; top: 155px; font-family: "Fira Sans", sans-serif; font-weight: 600;
    font-size: 22px; color: var(--white); }

  .steps-line { position: absolute; left: 67px; top: 245px; width: 2px; height: 205px; background: #e9f1d4; }
  .step { position: absolute; left: 54px; display: flex; gap: 20px; }
  .step-dot { width: 27px; height: 27px; border-radius: 50%; border: 2px solid #eef4dc; flex: none; margin-top: 4px; }
  .step-title { font-size: 24px; line-height: 28px; color: var(--white); }
  .step-sub { font-size: 17px; line-height: 20px; color: var(--white); }
  .step-1 { top: 232px; } .step-1 .step-dot { background: var(--dot-1); }
  .step-2 { top: 340px; } .step-2 .step-dot { background: var(--dot-2); }
  .step-3 { top: 436px; } .step-3 .step-dot { background: var(--dot-3); }

  .badge { position: absolute; left: 412px; top: 223px; width: 190px; height: 54px; background: var(--navy-deep);
    transform: rotate(-2deg); transform-origin: left top; color: var(--white);
    font-size: 13.5px; line-height: 17px; text-align: center; padding: 10px 14px 0 4px; }

  .rule { position: absolute; left: 0; top: 1013px; width: 100%; height: 5px; background: var(--navy-deep); }

  .footer { position: absolute; left: 0; top: 1018px; width: 100%; height: 142px; background: var(--footer); }
  .partners-label { position: absolute; left: 53px; top: 20px; font-size: 17px; color: var(--navy); }
  .partners { position: absolute; left: 53px; right: 50px; top: 76px; display: flex; justify-content: space-between; align-items: center; }
  .partner { display: flex; align-items: center; gap: 5px; font-size: 11px; color: var(--navy); }
  .partner-mark { width: 14px; height: 14px; border-radius: 50%; background: #8c96a8; }
</style>
</head>
<body>
  <main class="banner">
    <header class="header">
      <div class="brand">
        <span class="brand-dot"></span>
        <div>
          <div class="brand-name">NVHS</div>
          <div class="brand-sub">Nordische Vereinigung für<br>Heitere Seelenkunde</div>
        </div>
      </div>
      <div class="site-url">www.freudenpfad.de</div>
    </header>

    <section class="hero">
      <div class="hero-photo" role="img" aria-label="Foto eines nachdenklichen jungen Mannes mit Locken und hellblauem Hemd"></div>
      <h1 class="headline">Sind Sie glücklich?</h1>
    </section>

    <section class="content">
      <p class="questions">Haben Sie noch unentdeckte Fähigkeiten?<br>Ist Ihr Leben erfüllt?<br>Oder gibt es da noch mehr?</p>
      <p class="answer-lead">Antworten finden Sie bei den Freudenpfad-Forschern:</p>

      <div class="steps-line"></div>
      <div class="step step-1">
        <span class="step-dot"></span>
        <div><div class="step-title">Online-Fragebogen ausfüllen</div><div class="step-sub">unter www.freudenpfad.de</div></div>
      </div>
      <div class="badge">wissenschaftlich evaluiert<br>kostenfrei | anonym</div>
      <div class="step step-2">
        <span class="step-dot"></span>
        <div><div class="step-title">Persönliche Rückmeldung erhalten</div><div class="step-sub">über das eigene Potenzial, Stärken und Möglichkeiten</div></div>
      </div>
      <div class="step step-3">
        <span class="step-dot"></span>
        <div><div class="step-title">Ein noch erfüllteres Leben leben</div><div class="step-sub">mit unseren Ratschlägen</div></div>
      </div>
    </section>

    <div class="rule"></div>

    <footer class="footer">
      <div class="partners-label">Forschungskooperationspartner</div>
      <div class="partners">
        <div class="partner"><span class="partner-mark"></span>Uni Wendelstein</div>
        <div class="partner"><span class="partner-mark"></span>Health Academy Marbach</div>
        <div class="partner"><span class="partner-mark"></span>HK-Lindau</div>
        <div class="partner"><span class="partner-mark"></span>Uni Falkenried</div>
      </div>
    </footer>
  </main>
</body>
</html>
```